Business card for builder specialising in renovations.

Need a card for our building business. Business name is under Martin Pelloe.
Have licence number on card ( 527916K)
Contact number (0400 382 615)
Want to work on logo for some business cards and shirts - something with MP or MPB or open to ideas??
No animations, No hammers. Something sharp and eye catching.
Highlight that we are a renovation specialist. Simple on front with extra details on back with some lines to jot down things.

Target Market(s)

Renovators

Industry/Entity Type

Building

Contact Information for Business Card

2 sided with room on back to jot things down.
Extra details on back so front can be simple ..like, renovations, bathrooms, decks, extensions, new builds,

Logo Text

MP

Font styles to use
Serif

Requirements
Must have
• Eye catching design .
• Name : Martin pelloe
• Licence number
• Contact number - 0400382615
Nice to have
• Some logo design that we can carry through to other forms of advertising
• Local builder
• Quality work
Should not have
• No animations

```html
<!DOCTYPE html>
<html lang="en">
<head>
<meta charset="utf-8">
<title>Martin Pelloe – Business Card</title>
<link rel="stylesheet" href="https://fonts.googleapis.com/css2?family=Lato:wght@400;700&family=Oxanium:wght@600&display=swap">
<style>
  :root {
    --page: #e8e9eb;
    --ink: #231f20;
    --red: #e31b23;
    --paper: #ffffff;
    --text-light: #f2f2f2;
  }
  html, body {
    margin: 0;
    width: 1200px;
    height: 900px;
    overflow: hidden;
    background: var(--page);
  }
  .sheet {
    width: 1200px;
    height: 900px;
    display: flex;
    align-items: center;
    justify-content: center;
    gap: 50px;
  }
  .card {
    position: relative;
    width: 525px;
    height: 300px;
    overflow: hidden;
    box-shadow: 0 2px 0 #cfd0d2, 0 4px 0 #dcdddf, 0 10px 24px rgba(0,0,0,0.12);
  }

  /* Front */
  .card-front { background: var(--ink); color: var(--text-light); }
  .front-graphic { position: absolute; inset: 0; }
  .brand {
    position: absolute;
    left: 40px;
    top: 122px;
    display: flex;
    align-items: center;
    gap: 14px;
  }
  .brand-mark {
    width: 34px;
    height: 34px;
    background: var(--red);
    display: flex;
    align-items: center;
    justify-content: center;
    font-family: "Oxanium", sans-serif;
    font-weight: 600;
    font-size: 17px;
    color: var(--paper);
  }
  .brand-name {
    font-family: "Oxanium", sans-serif;
    font-weight: 600;
    font-size: 24px;
    letter-spacing: 1.5px;
    color: var(--paper);
  }
  .front-details {
    position: absolute;
    left: 40px;
    bottom: 36px;
    font-family: "Lato", sans-serif;
    font-size: 15px;
    line-height: 1.45;
    letter-spacing: 0.6px;
  }

  /* Back */
  .card-back { background: var(--paper); color: var(--ink); }
  .rule-black {
    position: absolute;
    left: 36px;
    top: 0;
    width: 6px;
    height: 82px;
    background: var(--ink);
  }
  .back-mark {
    position: absolute;
    left: 56px;
    top: 24px;
    width: 30px;
    height: 30px;
    background: var(--red);
    display: flex;
    align-items: center;
    justify-content: center;
    font-family: "Oxanium", sans-serif;
    font-weight: 600;
    font-size: 14px;
    color: var(--paper);
  }
  .rule-red {
    position: absolute;
    left: 68px;
    top: 74px;
    width: 5px;
    height: 226px;
    background: var(--red);
  }
  .tagline {
    position: absolute;
    left: 40px;
    bottom: 18px;
    writing-mode: vertical-rl;
    transform: rotate(180deg);
    font-family: "Lato", sans-serif;
    font-weight: 700;
    font-size: 15px;
    letter-spacing: 1px;
  }
  .services {
    position: absolute;
    left: 90px;
    top: 78px;
    margin: 0;
    padding: 0;
    list-style: none;
    font-family: "Lato", sans-serif;
    font-size: 19px;
    line-height: 1.3;
    letter-spacing: 0.4px;
  }
</style>
</head>
<body>
<main class="sheet">

  <section class="card card-front" aria-label="Card front">
    <svg class="front-graphic" viewBox="0 0 525 300" width="525" height="300" aria-hidden="true">
      <polygon points="300,0 360,0 330,70 245,70" fill="var(--paper)"/>
      <polygon points="385,0 420,0 370,110 345,90" fill="var(--paper)"/>
      <polygon points="372,0 380,0 335,100 325,96" fill="var(--ink)"/>
      <polygon points="430,0 525,0 525,300 420,300 470,180 400,110" fill="var(--red)"/>
      <polygon points="395,115 410,120 470,180 462,190" fill="var(--ink)"/>
      <polygon points="470,0 485,0 525,95 525,130" fill="var(--ink)"/>
      <polygon points="485,190 525,150 525,300 440,300" fill="var(--ink)"/>
    </svg>
    <div class="brand">
      <div class="brand-mark">MP</div>
      <div class="brand-name">Martin Pelloe</div>
    </div>
    <div class="front-details">
      <div>Contact : 0400 382 615</div>
      <div>Licence Number : 527916K</div>
    </div>
  </section>

  <section class="card card-back" aria-label="Card back">
    <div class="rule-black"></div>
    <div class="back-mark">MP</div>
    <div class="rule-red"></div>
    <div class="tagline">Renovate with us......</div>
    <ul class="services">
      <li>Renovations</li>
      <li>Bathrooms</li>
      <li>Decks</li>
      <li>Extensions</li>
      <li>New Builds etc</li>
    </ul>
  </section>

</main>
</body>
</html>
```